Fine Art business needs new website

We need a simple website with a home page, about us page, New sculptures, Sold sculptures, and a contact us page.Our sculptures are very high end one of a kind pieces. As such we need the site to be VERY elegant and professional. Lastly, because I'll be updating pictures on the website on a monthly basis it needs to be user friendly to update (Wordpress is preferred). The only branding we have so far for the business is a business card.
Updates
I wasn't completely ready when this project launched, also I am on the road right now and haven't been able to be as responsive to all you designers as I would like. I will work on giving feedback to all the top designs we've received so far. Thank you all so much for your participation and hardwork.
Target Market(s)
High end customers (affluent), art collectors, interior decorators/designers
Industry/Entity Type
Art Gallery
Coding
Coded - Design and coding required
Number of Pages Required
5+ page
Requirements
Must have
- Easily editable picture gallery for myself so that I can add new pieces(pictures of the pieces), remove sold pieces, etc. I would like the website to be built in wordpress so I can update it. I currently use sitekeeperpro through Netbirch for my other business website and would like to do the same for this one.
- Pages:
- -Intro page with featured pieces
- -Current pieces gallery (for sale) mainly a picture gallery
- -Sculptures archive (sold pieces) another picture gallery
- -About us: Pull-down of -about the artist (attached content)
- -Artistic Process (attached content)
- -Show Schedule:
- -one page dedicated to "friends of QMW" (basically a link page)
- TO BE CLEAR "www.lanternhollow.com" IS A TOTALLY DIFFERENT SITE AND I'M NOT TRYING TO COMBINE THE TWO OR JOIN THEM INTO ONE. This page needs be more elegant and seperate from the Lantern Hollow site.
- UPDATE: I'd like a link to the QMW Facebook page: https://www.facebook.com/quillmarkworks/
Nice to have
- I would like the pictures on the gallery pages able to have text connected with them (Materials, price)
- I would like the site style and fonts to be similar to our business cards we've already had designed (picture attached).
Should not have
- Too much flash or other things that will make the site slow to load.

```html
<!DOCTYPE html>
<html lang="en">
<head>
<meta charset="utf-8">
<title>Quillmark Works</title>
<link rel="stylesheet" href="https://fonts.googleapis.com/css2?family=Cinzel:wght@400;700&family=Montserrat:wght@400;500;600&family=Poppins:ital,wght@0,400;1,500&display=swap">
<style>
:root{
  --ink:#222;
  --muted:#666;
  --line:#d9d9d9;
  --plum:#3d1b47;
  --plum-deep:#2f1238;
  --violet:#5b2a7a;
  --card:#f2f2f2;
  --white:#fff;
  --dark:#111;
}
*{box-sizing:border-box;margin:0;padding:0}
html,body{width:1200px;height:3109px;overflow:hidden;background:var(--white);color:var(--ink);font-family:"Montserrat",sans-serif}
.page{position:relative;width:1200px;height:3109px}
.abs{position:absolute}
.serif{font-family:"Cinzel",serif}

/* header */
.contact-item{position:absolute;left:100px;display:flex;align-items:center;gap:16px;font-size:13px;color:var(--muted)}
.contact-icon{width:26px;height:26px;border:1px solid #999;border-radius:50%;display:flex;align-items:center;justify-content:center}
.brand{position:absolute;left:435px;top:20px;width:332px;height:150px;display:flex;flex-direction:column;align-items:center;justify-content:center;gap:14px}
.brand-mark{width:64px;height:64px;border-radius:50%;background:linear-gradient(135deg,#6a3a8e,#2b1137)}
.brand-name{font-family:"Cinzel",serif;font-size:19px;letter-spacing:3px;color:#333}
.social{position:absolute;display:flex;gap:16px}
.social span{width:38px;height:38px;border-radius:50%;display:block}
.s1{background:#4b2a8a}.s2{background:#6b2d6e}.s3{background:#a3232f}.s4{background:#1f4f99;display:flex!important;align-items:center;justify-content:center}
.nav{position:absolute;top:186px;left:0;width:1200px;height:52px;border-top:1px solid var(--line);display:flex;justify-content:center;align-items:center;gap:0}
.nav a{font-family:"Cinzel",serif;font-size:14px;color:#222;text-decoration:none;padding:0 32px;letter-spacing:.5px}

/* hero */
.hero{position:absolute;top:238px;left:0;width:1200px;height:487px;background:radial-gradient(ellipse at 30% 30%,#7b4fa3 0%,#3e1d5a 45%,#1a0a24 100%);display:flex;align-items:center;justify-content:center}
.hero h1{font-family:"Cinzel",serif;font-weight:700;font-size:64px;color:#fff;letter-spacing:1px}

.section-title{position:absolute;left:0;width:1200px;text-align:center;font-family:"Cinzel",serif;font-size:44px;font-weight:400;color:#222;letter-spacing:1px}

/* featured */
.piece{position:absolute;background:var(--card)}
.piece-photo{position:absolute;left:0;top:0;width:100%;background:radial-gradient(ellipse at 50% 55%,#3a2c24 0%,#111 70%)}
.piece-label{position:absolute;left:0;bottom:0;width:100%;height:52px;display:flex;justify-content:space-between;align-items:center;padding:0 20px}
.piece-label b{font-weight:600;font-size:18px;letter-spacing:.5px}
.piece-label i{font-style:normal;font-size:14px}

/* blog */
.post{position:absolute;top:1632px;width:313px;height:451px;background:#f7f7f7}
.post.raised{box-shadow:0 4px 14px rgba(0,0,0,.18)}
.post-photo{height:198px;background:radial-gradient(ellipse at 50% 55%,#3b3b3b 0%,#0f0f0f 70%)}
.post-meta{position:absolute;left:10px;top:218px;font-family:"Cinzel",serif;font-size:12px;color:#333}
.post-meta em{font-style:normal;margin:0 10px;color:#888}
.post-title{position:absolute;left:10px;top:244px;width:270px;font-family:"Poppins",sans-serif;font-style:italic;font-weight:500;font-size:15px;line-height:23px;color:#222}
.post-text{position:absolute;left:10px;top:306px;width:290px;font-size:11px;line-height:21px;color:#777}
.post-btn{position:absolute;left:11px;top:393px;width:160px;height:42px;background:var(--plum);color:#fff;font-size:12px;font-weight:600;display:flex;align-items:center;justify-content:center;gap:14px}
.post-share{position:absolute;right:12px;top:408px;font-size:11px;color:#333;display:flex;gap:8px;align-items:center}

/* schedule */
.schedule{position:absolute;top:2187px;left:0;width:1200px;height:390px;background:var(--plum)}
.schedule-photo{position:absolute;left:0;top:0;width:311px;height:390px;background:radial-gradient(ellipse at 50% 45%,#4b2a6e 0%,#1a0f1f 70%)}
.avatar{position:absolute;left:377px;top:2344px;width:112px;height:112px;border-radius:50%;background:#c9b8a8;border:4px solid #fff}
.date-tag{position:absolute;left:531px;top:2344px;width:124px;height:26px;background:#fff;color:#222;font-size:12px;font-weight:600;display:flex;align-items:center;justify-content:center}
.schedule-text{position:absolute;left:531px;top:2388px;width:560px;font-size:13.5px;line-height:27px;color:#fff}
.schedule-by{position:absolute;left:531px;top:2484px;font-family:"Cinzel",serif;font-size:13px;color:#fff}
.dots{position:absolute;left:412px;top:2504px;display:flex;gap:7px}
.dots span{width:6px;height:6px;border-radius:50%;background:#fff}

/* footer */
.footer-brand{position:absolute;left:500px;top:2630px;width:200px;display:flex;flex-direction:column;align-items:center;gap:10px}
.footer-brand .brand-mark{width:50px;height:50px}
.footer-brand .brand-name{font-size:13px}
.footer-title{position:absolute;top:2750px;left:0;width:1200px;text-align:center;font-family:"Cinzel",serif;font-size:28px;color:#222}
.footer-text{position:absolute;top:2800px;left:370px;width:460px;text-align:center;font-size:14px;line-height:27px;color:#333}
.signup{position:absolute;top:2879px;left:371px;width:458px;height:44px;display:flex}
.signup input{flex:1;border:1px solid #999;border-right:none;padding:0 14px;font-family:"Montserrat",sans-serif;font-size:14px;color:#666;background:#fff}
.signup button{width:128px;border:none;background:var(--plum);color:#fff;font-family:"Montserrat",sans-serif;font-size:14px;letter-spacing:1.5px}
.copyright{position:absolute;top:3072px;left:0;width:1200px;text-align:center;font-size:12px;color:#555}
</style>
</head>
<body>
<div class="page">

<header>
  <div class="contact-item" style="top:11px">
    <span class="contact-icon"><svg width="12" height="12" viewBox="0 0 24 24"><path d="M6.6 10.8a15 15 0 0 0 6.6 6.6l2.2-2.2c.3-.3.7-.4 1-.2 1.1.4 2.3.6 3.6.6.6 0 1 .4 1 1V20c0 .6-.4 1-1 1A17 17 0 0 1 3 4c0-.6.4-1 1-1h3.5c.6 0 1 .4 1 1 0 1.3.2 2.5.6 3.6.1.3 0 .7-.2 1z" fill="#555"/></svg></span>(555) 214-0398
  </div>
  <div class="contact-item" style="top:48px">
    <span class="contact-icon"><svg width="12" height="10" viewBox="0 0 24 18"><rect x="1" y="1" width="22" height="16" fill="#555"/><path d="M1 1l11 9 11-9" stroke="#fff" stroke-width="2" fill="none"/></svg></span>hello@lanternhollow.com
  </div>
  <div class="brand"><span class="brand-mark"></span><span class="brand-name">QUILLMARK WORKS</span></div>
  <div class="social" style="left:900px;top:5px">
    <span class="s1" aria-label="Social profile"></span><span class="s2" aria-label="Social profile"></span><span class="s3" aria-label="Social profile"></span>
    <span class="s4" aria-label="Email"><svg width="16" height="12" viewBox="0 0 24 18"><rect x="1" y="1" width="22" height="16" fill="#fff"/><path d="M1 1l11 9 11-9" stroke="#1f4f99" stroke-width="2" fill="none"/></svg></span>
  </div>
  <nav class="nav">
    <a>HOME</a><a>ABOUT US</a><a>NEW SCULPTURES</a><a>SOLD SCULPTURES</a><a>CONTACT US</a>
    <a><svg width="13" height="13" viewBox="0 0 24 24"><circle cx="10" cy="10" r="7" stroke="#222" stroke-width="3" fill="none"/><path d="M15 15l7 7" stroke="#222" stroke-width="3"/></svg></a>
  </nav>
</header>

<section class="hero" role="img" aria-label="Close-up of purple amethyst crystals"><h1>QUILLMARK WORKS</h1></section>

<h2 class="section-title" style="top:812px">FEATURED PIECES</h2>
<div class="piece" style="left:100px;top:904px;width:331px;height:267px"><div class="piece-photo" style="height:215px" role="img" aria-label="Amethyst geode sculpture on a stand"></div><div class="piece-label"><b>SCULPTURE</b><i>$12.00</i></div></div>
<div class="piece" style="left:100px;top:1173px;width:331px;height:264px"><div class="piece-photo" style="height:212px" role="img" aria-label="Swirling golden stone sculpture"></div><div class="piece-label"><b>SCULPTURE</b><i>$102.00</i></div></div>
<div class="piece" style="left:435px;top:904px;width:268px;height:533px"><div class="piece-photo" style="height:481px;background:radial-gradient(ellipse at 50% 50%,#2e5a3a 0%,#111 60%)" role="img" aria-label="Tall green jade sculpture on a black base"></div><div class="piece-label"><b>SCULPTURE</b><i>$102.00</i></div></div>
<div class="piece" style="left:705px;top:904px;width:395px;height:267px"><div class="piece-photo" style="height:215px;background:radial-gradient(ellipse at 50% 55%,#6a3a1c 0%,#111 65%)" role="img" aria-label="Orange crystal geode sculpture"></div><div class="piece-label"><b>SCULPTURE</b><i>$102.00</i></div></div>
<div class="piece" style="left:705px;top:1173px;width:395px;height:264px"><div class="piece-photo" style="height:212px" role="img" aria-label="Ammonite fossil sculpture with curved horns"></div><div class="piece-label"><b>SCULPTURE</b><i>$102.00</i></div></div>

<h2 class="section-title" style="top:1527px">FROM THE BLOG</h2>
<svg class="abs" style="left:40px;top:1835px" width="22" height="44" viewBox="0 0 22 44"><path d="M20 2L2 22l18 20" stroke="#444" stroke-width="2" fill="none"/></svg>
<svg class="abs" style="left:1138px;top:1835px" width="22" height="44" viewBox="0 0 22 44"><path d="M2 2l18 20L2 42" stroke="#222" stroke-width="2" fill="none"/></svg>

<article class="post raised" style="left:100px"><div class="post-photo" role="img" aria-label="Green malachite sculpture"></div>
  <p class="post-meta">QUILLMARK WORKS<em>/</em>03.01.2018</p><h3 class="post-title">Sed ut perspiciatis unde omnis iste natus error</h3>
  <p class="post-text">Sed ut perspiciatis unde omnis iste natus error sit voluptatem accusantium doloremque tium, totam rem...</p>
  <span class="post-btn">KEEP READING <span>&rsaquo;</span></span><span class="post-share"><svg width="11" height="11" viewBox="0 0 24 24"><circle cx="18" cy="5" r="4"/><circle cx="6" cy="12" r="4"/><circle cx="18" cy="19" r="4"/><path d="M6 12l12-7M6 12l12 7" stroke="#000" stroke-width="2"/></svg>5</span></article>
<article class="post" style="left:444px"><div class="post-photo" role="img" aria-label="Pale carved stone sculpture"></div>
  <p class="post-meta">QUILLMARK WORKS<em>/</em>03.01.2018</p><h3 class="post-title">Sed ut perspiciatis unde omnis iste natus error</h3>
  <p class="post-text">Sed ut perspiciatis unde omnis iste natus error sit voluptatem accusantium doloremque tium, totam rem...</p>
  <span class="post-btn">KEEP READING <span>&rsaquo;</span></span><span class="post-share"><svg width="11" height="11" viewBox="0 0 24 24"><circle cx="18" cy="5" r="4"/><circle cx="6" cy="12" r="4"/><circle cx="18" cy="19" r="4"/><path d="M6 12l12-7M6 12l12 7" stroke="#000" stroke-width="2"/></svg>5</span></article>
<article class="post" style="left:788px"><div class="post-photo" style="background:radial-gradient(ellipse at 50% 55%,#2a3a6a 0%,#0f0f0f 70%)" role="img" aria-label="Blue twisted stone sculpture"></div>
  <p class="post-meta">QUILLMARK WORKS<em>/</em>03.01.2018</p><h3 class="post-title">Sed ut perspiciatis unde omnis iste natus error</h3>
  <p class="post-text">Sed ut perspiciatis unde omnis iste natus error sit voluptatem accusantium doloremque tium, totam rem...</p>
  <span class="post-btn">KEEP READING <span>&rsaquo;</span></span><span class="post-share"><svg width="11" height="11" viewBox="0 0 24 24"><circle cx="18" cy="5" r="4"/><circle cx="6" cy="12" r="4"/><circle cx="18" cy="19" r="4"/><path d="M6 12l12-7M6 12l12 7" stroke="#000" stroke-width="2"/></svg>5</span></article>

<section class="schedule">
  <div class="schedule-photo" role="img" aria-label="Amethyst geode ring sculpture on a gold stand"></div>
  <h2 class="abs serif" style="left:386px;top:72px;font-size:42px;font-weight:400;color:#fff">SHOW SCHEDULE</h2>
</section>
<div class="avatar" role="img" aria-label="Portrait of the artist"></div>
<div class="date-tag">AUG 2018, 11-12</div>
<p class="schedule-text">Lorem ipsum dolor sit amet, consectetur adipiscing elit, sed do eiusmod tempor incididunt ut labore et dolore magna aliqua. Ut enim adamco laboris nisi ut aliquip ex ea commodo consequat...read more</p>
<p class="schedule-by">-ART FAIR CEDAR BASIN</p>
<div class="dots"><span></span><span></span><span></span></div>

<footer>
  <div class="footer-brand"><span class="brand-mark"></span><span class="brand-name">QUILLMARK WORKS</span></div>
  <h2 class="footer-title">Get In Touch With Us</h2>
  <p class="footer-text">At vero eos et accusamus et iusto odio dignissimos ducimus qui blanditiis praesentium voluptatum deleniti atque</p>
  <form class="signup"><input type="text" value="Enter Your Email Address"><button type="button">SUBSCRIBE</button></form>
  <div class="social" style="left:502px;top:2950px;gap:16px">
    <span class="s1" style="width:36px;height:36px" aria-label="Social profile"></span><span class="s2" style="width:36px;height:36px" aria-label="Social profile"></span><span class="s3" style="width:36px;height:36px" aria-label="Social profile"></span>
    <span class="s4" style="width:36px;height:36px" aria-label="Email"><svg width="16" height="12" viewBox="0 0 24 18"><rect x="1" y="1" width="22" height="16" fill="#fff"/><path d="M1 1l11 9 11-9" stroke="#1f4f99" stroke-width="2" fill="none"/></svg></span>
  </div>
  <p class="copyright">&copy; Copyrights 2018 Quillmark Works All Rights Reserved</p>
</footer>

</div>
</body>
</html>
```